Business Identity Stationary

Already have the logo which is in the attached files so only need the Business STationary
1) Double Sided Business Card
2) Letterhead
3) Presentation folder with business card holder on inside cover
4) WIth compliments slip
See information for business cards, letterhead and presentation folder below.
http://files.pixelbazaar-example.com/img/771204/40612/40612_3918825_771204_thumb.jpg
Updates

This should be a simply job using a logo we already had designed along with a little device. I suggest using the device off center and perhaps lower in the corner in an abstract way. Also the logo device could be used as a watermark for the letterhead. The designer who created the logo presented something that I think works well for a business card. The front of the double sided business card could have the name logo small for the website address and only use the Lime device on the front. Then on the back could be the name Brevar Consulting logo.

Please note that for the business card the black and lime green background do look good. Also please think of using the lime device separately in an unusual way.

It has been brought to my attention that.my budget was far to low. Hopefully this.will attract you to the project. 

The parent company of Brevar Consulting is TallHeron investments. I have uploaded a file of the Tall Heron business card I really like. Perhaps use this business card as a guide to the type of modern and clean style I am looking for. It also works to have the Brevar Consultign and Tall Heron similar.

Reason: Still haven't received anything exactly right.

Industry/Entity Type

Business

Font styles to use
Sans Serif

Colors
9bcb3c
000000
5c5c5c
add136
cadf82
eaf2cf
f9fbf2
1b1b1b
757575

Requirements
Must have
• 1) Double Sided Business Card
Marta Delvorin
Director
Tel: +505 8290 3357
Email: mkd@brevarconsulting-example.com
Website: www.brevarconsulting-example.com

Everett Delvorin
Director
Tel: +505 8290 3362
Email: ekd@brevarconsulting-example.com

Lucia Pardo Ventrosa
Director
Tel: 8442 6183
Email: lpv@brevarconsulting-example.com

2) Letterhead
Logo
Lime Logo Device
Website Address: www.brevarconsulting-example.com
Small print on bottom: Brevar Consulting a Tall Heron Investment Company SA. RUC K0720000483915

3) Presentation Folder
Traditional Presentation folder with inside front cover spot for the insertion of business card.

4) With Compliments slip

```html
<!DOCTYPE html>
<html lang="en">
<head>
<meta charset="utf-8">
<title>Brevar Consulting – Stationery</title>
<link rel="stylesheet" href="https://fonts.googleapis.com/css2?family=Open+Sans:wght@300;400;700&display=swap">
<style>
  :root {
    --canvas: #f4f9ee;
    --black: #000000;
    --paper: #ffffff;
    --lime: #7ee82a;
    --lime-name: #a6f22e;
    --leaf-strip: #4a8a0c;
    --watermark: #e6f7e4;
    --grey-text: #8a8a8a;
    --ink: #1b1b1b;
    --rule: #5c5c5c;
  }
  * { box-sizing: border-box; margin: 0; padding: 0; }
  html, body { width: 1200px; height: 1000px; overflow: hidden; }
  body {
    background: var(--canvas);
    font-family: "Open Sans", Arial, sans-serif;
    position: relative;
  }
  .sheet {
    position: absolute;
    background: var(--paper);
    box-shadow: 3px 4px 7px rgba(0,0,0,0.45);
    overflow: hidden;
  }
  .header-band { position: absolute; left: 0; right: 0; top: 0; background: var(--black); }
  .foot-strip { position: absolute; left: 0; right: 0; bottom: 0; background: var(--leaf-strip); }
  .brand {
    position: absolute;
    display: flex; align-items: center;
    color: #ffffff;
    font-weight: 300;
    letter-spacing: 0.02em;
    white-space: nowrap;
  }
  .brand-dot { border-radius: 50%; background: var(--lime); margin-left: 0.35em; flex: none; }
  .corner-dot { position: absolute; border-radius: 50%; background: var(--lime); }
  .legal {
    position: absolute; text-align: center;
    font-size: 5.5px; line-height: 9px; color: var(--ink); font-weight: 700;
  }

  /* letterhead */
  .letterhead { left: 25px; top: 42px; width: 370px; height: 479px; }
  .letterhead .header-band { height: 44px; }
  .letterhead .brand { left: 8px; top: 13px; font-size: 15px; }
  .letterhead .watermark {
    position: absolute; left: 65px; top: 171px; width: 210px; height: 210px;
    border-radius: 50%; background: var(--watermark);
  }
  .letterhead .legal { left: 0; right: 0; top: 454px; }
  .letterhead .foot-strip { height: 5px; }

  /* folder */
  .folder { left: 420px; top: 42px; width: 762px; height: 480px; }
  .folder .header-band { height: 74px; }
  .folder .brand { top: 24px; font-size: 26px; }
  .folder .brand.left-panel { left: 16px; }
  .folder .brand.right-panel { left: 396px; }
  .folder .fold-line { position: absolute; left: 380px; top: 74px; bottom: 0; width: 2px; background: #8c8c8c; }
  .folder .legal { left: 0; width: 380px; top: 455px; }
  .folder .foot-strip { height: 5px; }
  .card-slot {
    position: absolute; left: 542px; top: 313px; width: 158px; height: 103px;
    border: 1px solid #7a7a7a; background: var(--paper);
  }

  /* compliments slip */
  .slip { left: 388px; top: 556px; width: 448px; height: 204px; }
  .slip .header-band { height: 52px; }
  .slip .brand { left: 12px; top: 17px; font-size: 15px; }
  .slip .greeting { position: absolute; left: 64px; top: 65px; font-size: 7.5px; font-weight: 700; color: var(--ink); }
  .slip .web { position: absolute; left: 9px; top: 184px; font-size: 7px; font-weight: 700; color: var(--ink); }
  .slip .foot-strip { height: 6px; }

  /* business cards */
  .card { background: var(--black); }
  .card .foot-strip { height: 10px; }
  .card .brand { left: 7px; top: 16px; font-size: 17px; }
  .card .person { position: absolute; left: 7px; top: 78px; color: var(--lime-name); }
  .card .person-name { font-size: 11.5px; font-weight: 700; line-height: 16px; }
  .card .person-role { font-size: 10px; line-height: 15px; }
  .card .contacts { position: absolute; left: 8px; top: 114px; list-style: none; }
  .card .contacts li {
    display: flex; align-items: center; gap: 7px;
    font-size: 9.5px; line-height: 14.3px; color: var(--grey-text); white-space: nowrap;
  }
  .card .contacts svg { width: 12px; height: 10px; flex: none; }
  .card .corner-dot { width: 56px; height: 56px; right: 5px; bottom: 3px; }
  .card-a { left: 25px; top: 793px; width: 275px; height: 170px; }
  .card-b { left: 318px; top: 793px; width: 277px; height: 170px; }
  .card-c { left: 612px; top: 793px; width: 279px; height: 170px; }
  .card-back { left: 904px; top: 793px; width: 278px; height: 170px; }
  .card-back .brand { left: 0; right: 0; top: 62px; justify-content: center; font-size: 24px; }
  .card-slot .card { position: absolute; left: 5px; top: 5px; width: 148px; height: 92px; box-shadow: none; }
  .card-slot .brand { left: 4px; top: 8px; font-size: 9px; }
  .card-slot .person { left: 4px; top: 42px; }
  .card-slot .person-name { font-size: 6px; line-height: 8px; }
  .card-slot .person-role { font-size: 5.5px; line-height: 7px; }
  .card-slot .contacts { left: 4px; top: 61px; }
  .card-slot .contacts li { font-size: 5px; line-height: 8px; gap: 4px; }
  .card-slot .contacts svg { width: 6px; height: 5px; }
  .card-slot .corner-dot { width: 26px; height: 26px; right: 6px; bottom: 4px; }
  .card-slot .foot-strip { height: 5px; }
</style>
</head>
<body>

<!-- Letterhead -->
<section class="sheet letterhead" aria-label="Letterhead">
  <div class="header-band"><div class="brand">Brevar Consulting<span class="brand-dot" style="width:9px;height:9px"></span></div></div>
  <div class="watermark" aria-hidden="true"></div>
  <p class="legal">www.brevarconsulting-example.com<br>Brevar Consulting a Tall Heron Investment Company SA. RUC K0720000483915</p>
  <div class="corner-dot" style="left:333px;top:450px;width:28px;height:28px"></div>
  <div class="foot-strip"></div>
</section>

<!-- Presentation folder -->
<section class="sheet folder" aria-label="Presentation folder">
  <div class="header-band">
    <div class="brand left-panel">Brevar Consulting<span class="brand-dot" style="width:15px;height:15px"></span></div>
    <div class="brand right-panel">Brevar Consulting<span class="brand-dot" style="width:15px;height:15px"></span></div>
  </div>
  <div class="fold-line"></div>
  <p class="legal">www.brevarconsulting-example.com<br>Brevar Consulting a Tall Heron Investment Company SA. RUC K0720000483915</p>
  <div class="card-slot">
    <div class="sheet card">
      <div class="brand">Brevar Consulting<span class="brand-dot" style="width:6px;height:6px"></span></div>
      <div class="person"><p class="person-name">Marta Delvorin</p><p class="person-role">Director</p></div>
      <ul class="contacts">
        <li><svg viewBox="0 0 12 10"><rect x="0.5" y="1" width="11" height="8" fill="#7ee82a"/><path d="M0.5 1 L6 6 L11.5 1" stroke="#000" fill="none"/></svg>mkd@brevarconsulting-example.com</li>
        <li><svg viewBox="0 0 12 10"><rect x="3" y="0" width="6" height="10" rx="1" fill="#7ee82a"/><rect x="4" y="1.5" width="4" height="3" fill="#000"/></svg>+505 8290 3357</li>
        <li><svg viewBox="0 0 12 10"><circle cx="6" cy="5" r="4.5" fill="#7ee82a"/></svg>www.brevarconsulting-example.com</li>
      </ul>
      <div class="corner-dot"></div>
      <div class="foot-strip"></div>
    </div>
  </div>
  <div class="corner-dot" style="left:718px;top:444px;width:34px;height:34px"></div>
  <div class="foot-strip"></div>
</section>

<!-- With compliments slip -->
<section class="sheet slip" aria-label="With compliments slip">
  <div class="header-band"><div class="brand">Brevar Consulting<span class="brand-dot" style="width:9px;height:9px"></span></div></div>
  <p class="greeting">With Compliments,</p>
  <p class="web">www.brevarconsulting-example.com</p>
  <div class="corner-dot" style="left:406px;top:167px;width:34px;height:34px"></div>
  <div class="foot-strip"></div>
</section>

<!-- Business cards, front -->
<section class="sheet card card-a" aria-label="Business card, Marta Delvorin">
  <div class="brand">Brevar Consulting<span class="brand-dot" style="width:10px;height:10px"></span></div>
  <div class="person"><p class="person-name">Marta Delvorin</p><p class="person-role">Director</p></div>
  <ul class="contacts">
    <li><svg viewBox="0 0 12 10"><rect x="0.5" y="1" width="11" height="8" fill="#7ee82a"/><path d="M0.5 1 L6 6 L11.5 1" stroke="#000" fill="none"/></svg>mkd@brevarconsulting-example.com</li>
    <li><svg viewBox="0 0 12 10"><rect x="3" y="0" width="6" height="10" rx="1" fill="#7ee82a"/><rect x="4" y="1.5" width="4" height="3" fill="#000"/></svg>+505 8290 3357</li>
    <li><svg viewBox="0 0 12 10"><circle cx="6" cy="5" r="4.5" fill="#7ee82a"/><path d="M1.5 5 H10.5 M6 0.5 V9.5" stroke="#000" stroke-width="0.8"/></svg>www.brevarconsulting-example.com</li>
  </ul>
  <div class="corner-dot"></div>
  <div class="foot-strip"></div>
</section>

<section class="sheet card card-b" aria-label="Business card, Everett Delvorin">
  <div class="brand">Brevar Consulting<span class="brand-dot" style="width:10px;height:10px"></span></div>
  <div class="person"><p class="person-name">Everett Delvorin</p><p class="person-role">Director</p></div>
  <ul class="contacts">
    <li><svg viewBox="0 0 12 10"><rect x="0.5" y="1" width="11" height="8" fill="#7ee82a"/><path d="M0.5 1 L6 6 L11.5 1" stroke="#000" fill="none"/></svg>ekd@brevarconsulting-example.com</li>
    <li><svg viewBox="0 0 12 10"><rect x="3" y="0" width="6" height="10" rx="1" fill="#7ee82a"/><rect x="4" y="1.5" width="4" height="3" fill="#000"/></svg>+505 8290 3362</li>
    <li><svg viewBox="0 0 12 10"><circle cx="6" cy="5" r="4.5" fill="#7ee82a"/><path d="M1.5 5 H10.5 M6 0.5 V9.5" stroke="#000" stroke-width="0.8"/></svg>www.brevarconsulting-example.com</li>
  </ul>
  <div class="corner-dot"></div>
  <div class="foot-strip"></div>
</section>

<section class="sheet card card-c" aria-label="Business card, Lucia Pardo Ventrosa">
  <div class="brand">Brevar Consulting<span class="brand-dot" style="width:10px;height:10px"></span></div>
  <div class="person"><p class="person-name">Lucia Pardo Ventrosa</p><p class="person-role">Director</p></div>
  <ul class="contacts">
    <li><svg viewBox="0 0 12 10"><rect x="0.5" y="1" width="11" height="8" fill="#7ee82a"/><path d="M0.5 1 L6 6 L11.5 1" stroke="#000" fill="none"/></svg>lpv@brevarconsulting-example.com</li>
    <li><svg viewBox="0 0 12 10"><rect x="3" y="0" width="6" height="10" rx="1" fill="#7ee82a"/><rect x="4" y="1.5" width="4" height="3" fill="#000"/></svg>+505 8442 6183</li>
    <li><svg viewBox="0 0 12 10"><circle cx="6" cy="5" r="4.5" fill="#7ee82a"/><path d="M1.5 5 H10.5 M6 0.5 V9.5" stroke="#000" stroke-width="0.8"/></svg>www.brevarconsulting-example.com</li>
  </ul>
  <div class="corner-dot"></div>
  <div class="foot-strip"></div>
</section>

<!-- Business card, back -->
<section class="sheet card card-back" aria-label="Business card, reverse">
  <div class="brand">Brevar Consulting<span class="brand-dot" style="width:14px;height:14px"></span></div>
  <div class="corner-dot" style="width:46px;height:46px;right:12px;bottom:3px"></div>
  <div class="foot-strip"></div>
</section>

</body>
</html>
```